Quick Straightforward Billboard Redesign

- Design billboard sized for 10 foot' x 36' foot width live area size and please include bleeds 6" around all sides
- Exact blue color match is imperative in headline, logo, phone number bubble or wherever used. C-83 / M-45 / Y-1 / K-0-
- What I hope to illustrate is that our company offers the best porch screening in the area area, in regards to quality, expertise, durability, storms proof, but we do not build screen porches.
- Current board is attached below from previous designer, and as you can see sizing was off, white space on edges make it appear to be sized incorrectly.
- I also attached my own little mock up idea well well if it helps, favorite image, logo, headline, etc and ideas perhaps on expanding or making this better?

Thanks so much!

Target Market(s)

Drivers and passengers, Southeastern NC, are of immense new construction and high end homes.

Industry/Entity Type

Construction

Colors
0054AA
0677BA
7BADD7
CADEEF
E8F1F8

Requirements
Must have
• Blue color matching
Nice to have
• Design spins or other thoughts on my little mock up

```html
<!DOCTYPE html>
<html lang="en">
<head>
<meta charset="utf-8">
<title>Bayhaven Porch Co. – Billboard</title>
<link rel="stylesheet" href="https://fonts.googleapis.com/css2?family=Anton&display=swap">
<style>
  :root {
    --brand-blue: #0058AE;
    --brand-green: #00AE4F;
    --band-cyan: #12B5E5;
    --paper: #FFFFFF;
    --stage: #E8F1F8;
    --photo-sky: #7BADD7;
    --photo-lawn: #9DBF6A;
    --photo-stone: #CFCBC3;
  }
  html, body {
    margin: 0;
    width: 1200px;
    height: 1200px;
    overflow: hidden;
    background: var(--stage);
  }
  .canvas {
    position: relative;
    width: 1200px;
    height: 1200px;
    display: flex;
    align-items: center;
    justify-content: center;
  }
  .billboard {
    width: 1120px;
    height: 311px;
    display: block;
    box-shadow: 0 10px 30px rgba(0, 40, 90, 0.18);
    background: var(--paper);
  }
  .headline, .brand-name, .phone-number {
    font-family: "Anton", "Oswald", sans-serif;
  }
  .headline--blue { fill: var(--brand-blue); }
  .headline--green { fill: var(--brand-green); }
  .brand-name { fill: var(--brand-blue); }
  .brand-mark { fill: var(--brand-blue); }
  .phone-band { fill: var(--band-cyan); }
  .phone-number { fill: var(--paper); }
  .phone-icon { fill: none; stroke: var(--paper); stroke-width: 4; stroke-linecap: round; stroke-linejoin: round; }
</style>
</head>
<body>
<main class="canvas">
  <svg class="billboard" viewBox="0 0 1120 311" xmlns="http://www.w3.org/2000/svg" aria-label="Bayhaven Porch Co. billboard">
    <defs>
      <linearGradient id="porchPhotoTone" x1="0" y1="0" x2="0" y2="1">
        <stop offset="0" stop-color="#F3F4F2"/>
        <stop offset="0.25" stop-color="var(--photo-sky)"/>
        <stop offset="0.5" stop-color="var(--photo-lawn)"/>
        <stop offset="0.62" stop-color="var(--photo-stone)"/>
        <stop offset="1" stop-color="#B9B2A7"/>
      </linearGradient>
    </defs>

    <rect class="board-paper" x="0" y="0" width="1120" height="311" fill="var(--paper)"/>

    <rect class="porch-photo" x="640" y="0" width="480" height="212" fill="url(#porchPhotoTone)"
          role="img" aria-label="Photo of a screened coastal porch with wicker furniture overlooking a lawn and lake"/>

    <text class="headline headline--blue" x="34" y="116" font-size="100" textLength="542" lengthAdjust="spacingAndGlyphs">Screen Your Porch</text>
    <text class="headline headline--green" x="30" y="218" font-size="100" textLength="545" lengthAdjust="spacingAndGlyphs">Built for the Coast</text>

    <rect class="brand-mark" x="30" y="249" width="38" height="38"/>
    <text class="brand-name" x="82" y="288" font-size="50" textLength="440" lengthAdjust="spacingAndGlyphs">BAYHAVEN PORCH CO.</text>

    <polygon class="phone-band" points="650,212 1120,212 1120,311 604,311"/>
    <g class="phone-icon" transform="translate(626,232)">
      <path d="M8 6 L16 4 L21 16 L15 20 Q18 32 28 40 L34 34 L46 40 L44 48 Q38 56 26 50 Q6 38 2 18 Q2 10 8 6 Z"/>
      <path d="M30 14 Q38 18 40 26"/>
      <path d="M32 4 Q46 10 50 24"/>
    </g>
    <text class="phone-number" x="686" y="292" font-size="82" textLength="410" lengthAdjust="spacingAndGlyphs">555.014.0199</text>
  </svg>
</main>
</body>
</html>
```